"Giggle Garden Days" Summer Camp flyer for preschool

I need a flyer for our preschool's summer camp. Our summer theme is GIGGLE garden DAYS. the theme MUST be displayed. We would like a mad scientist with crazy hair look with test tubes and goggles PROMINENTLY DISPLAYED on the flyer. this is for a preschool so we don't want the scientist to look scary. Our logo needs to be included on the flyer. The age range for the school is 6weeks to 6 years (you can add "6 weeks to 6 years" somewhere small on the flyer). Please add "Camp starts June 5th" and Sign up for 1 camp or all!". The weekly themes for the camp are ...
Journey into Outer Space
Rock Out in Geology
Weather
Water Extravagnaza
Biology
Physics - Force & Motion
Light
Sensational Sounds
Budding Builders
Krazy Kitchen Chemistry
Electromagnetism
It's Hip to Be Healthy
we don't want these on the flyer but maybe you can use them for image inspiration.
Attached is our logo and some verbiage that can be used.

moms and dads of preschool age kids

Preschool

• our logo, title of the camp, dates, a Mad Scientist with crazy hair, test tube, and goggles. attached is image of scientist. i will purchase this once art is approved.
• it would be nice to have the weekly themes on the flyer

```html
<!DOCTYPE html>
<html lang="en">
<head>
<meta charset="utf-8">
<title>Giggle Garden Days – Summer Camp</title>
<link rel="stylesheet" href="https://fonts.googleapis.com/css2?family=Montserrat:wght@400;500;700;800&family=Lato:wght@700;900&family=Anton&display=swap">
<style>
  :root {
    --navy: #0b2670;
    --sky: #94d8e6;
    --white: #ffffff;
    --yellow: #fbe33a;
    --lime: #8ff42c;
    --red: #e8241c;
    --ink: #1d1d1d;
    --stripe-dark: #2b2b2b;
    --stripe-light: #b5b5b5;
  }
  * { margin: 0; padding: 0; box-sizing: border-box; }
  html, body { width: 890px; height: 1200px; overflow: hidden; background: var(--sky); }
  .flyer { position: relative; width: 890px; height: 1200px; background: var(--sky); overflow: hidden; }

  .header { position: absolute; left: 0; top: 0; width: 890px; height: 277px; background: var(--navy); }
  .title { position: absolute; left: 44px; top: 40px; }
  .title-top {
    font-family: "Montserrat", sans-serif; font-weight: 800; font-size: 52px;
    color: var(--yellow); letter-spacing: 1px; line-height: 1;
  }
  .title-top .soft { text-transform: lowercase; }
  .title-main {
    font-family: "Anton", sans-serif; font-size: 128px; color: var(--lime);
    line-height: 1; margin-top: 12px; letter-spacing: 4px;
  }

  .scientist {
    position: absolute; left: 560px; top: 120px; width: 330px; height: 580px;
    background: linear-gradient(180deg, #f3f3f3 0%, #e9eef0 45%, #3b2f3a 80%, #1f6a74 100%);
    border-radius: 140px 140px 30px 30px; opacity: 0.92;
  }

  .schedule { position: absolute; left: 0; top: 303px; width: 571px; list-style: none; }
  .week { position: relative; height: 71.5px; }
  .week-bar {
    position: absolute; left: 0; top: 0; width: 571px; height: 52px; background: var(--white);
    display: flex; align-items: center;
  }
  .week-stripe {
    position: absolute; left: 0; top: 52px; width: 571px; height: 14px;
    background: linear-gradient(90deg, var(--stripe-dark) 0%, #6b6b6b 50%, var(--stripe-light) 100%);
    clip-path: polygon(0 0, 97% 0, 100% 100%, 0 100%);
  }
  .week-date {
    width: 238px; padding-left: 28px; font-family: "Lato", sans-serif; font-weight: 700;
    font-size: 27px; color: var(--red); white-space: nowrap;
  }
  .week-date.tight { padding-left: 22px; }
  .week-theme { font-family: "Lato", sans-serif; }
  .theme-name { font-weight: 700; font-size: 21px; color: var(--ink); line-height: 1.15; }
  .theme-tag { font-family: "Montserrat", sans-serif; font-weight: 500; font-size: 13px; color: var(--ink); margin-top: 3px; letter-spacing: 0.3px; }

  .camp-panel {
    position: absolute; left: 576px; top: 648px; width: 314px; height: 510px; background: var(--navy);
    display: flex; flex-direction: column; align-items: center; padding-top: 38px;
  }
  .camp-intro {
    font-family: "Montserrat", sans-serif; font-weight: 700; font-size: 46px; color: var(--yellow);
    text-align: center; line-height: 1.15;
  }
  .camp-season { font-family: "Anton", sans-serif; font-size: 72px; color: var(--yellow); line-height: 1; margin-top: 4px; }
  .camp-word { font-family: "Anton", sans-serif; font-size: 96px; color: var(--yellow); line-height: 1; letter-spacing: 2px; }
  .glassware {
    margin-top: 20px; width: 250px; height: 132px;
    background: linear-gradient(180deg, #dff3f8 0%, var(--sky) 100%); border-radius: 12px; opacity: 0.85;
  }

  .footer-band { position: absolute; left: 0; top: 1158px; width: 890px; height: 42px; background: var(--lime); }
</style>
</head>
<body>
<main class="flyer">
  <header class="header">
    <h1 class="title">
      <div class="title-top">GIGGLE <span class="soft">garden</span></div>
      <div class="title-main">DAYS</div>
    </h1>
  </header>

  <div class="scientist" role="img" aria-label="Cartoon scientist with wild white hair in a lab coat, holding a bubbling flask and a test tube"></div>

  <ol class="schedule">
    <li class="week"><div class="week-bar"><div class="week-date">June 5th - 9th</div><div class="week-theme"><div class="theme-name">[ Journey into Outer Space]</div><div class="theme-tag">As vast as the universe !</div></div></div><div class="week-stripe"></div></li>
    <li class="week"><div class="week-bar"><div class="week-date">June 12 - 16</div><div class="week-theme"><div class="theme-name">[ Rock Out in Geology ]</div><div class="theme-tag">Hard as a rock</div></div></div><div class="week-stripe"></div></li>
    <li class="week"><div class="week-bar"><div class="week-date">June 19 - 23</div><div class="week-theme"><div class="theme-name">[ Weather]</div><div class="theme-tag">When the fun blows in</div></div></div><div class="week-stripe"></div></li>
    <li class="week"><div class="week-bar"><div class="week-date">June 24 - 30</div><div class="week-theme"><div class="theme-name">[ Water Extravagnaza]</div><div class="theme-tag">Flowing with knowledge</div></div></div><div class="week-stripe"></div></li>
    <li class="week"><div class="week-bar"><div class="week-date">July 3 - 7</div><div class="week-theme"><div class="theme-name">[ Biology]</div><div class="theme-tag">Its alive !</div></div></div><div class="week-stripe"></div></li>
    <li class="week"><div class="week-bar"><div class="week-date">July 10 - 14</div><div class="week-theme"><div class="theme-name">[ Physics- Force &amp; Motion]</div><div class="theme-tag">Making Quantum leaps !</div></div></div><div class="week-stripe"></div></li>
    <li class="week"><div class="week-bar"><div class="week-date">July 17 - 21</div><div class="week-theme"><div class="theme-name">[ Light]</div><div class="theme-tag">Our future’s so bright we gotta wear shades!</div></div></div><div class="week-stripe"></div></li>
    <li class="week"><div class="week-bar"><div class="week-date">July 24 - 28</div><div class="week-theme"><div class="theme-name">[ Sensational Sounds ]</div><div class="theme-tag">Making Quantum leaps !</div></div></div><div class="week-stripe"></div></li>
    <li class="week"><div class="week-bar"><div class="week-date tight">July 31 - Aug 4</div><div class="week-theme"><div class="theme-name">[ Budding Builders]</div><div class="theme-tag">Making a tough job easier!</div></div></div><div class="week-stripe"></div></li>
    <li class="week"><div class="week-bar"><div class="week-date tight">Aug 7 - Aug 11</div><div class="week-theme"><div class="theme-name">[ Krazy Kitchen Chemistry ]</div><div class="theme-tag">Bubbling with excitement !</div></div></div><div class="week-stripe"></div></li>
    <li class="week"><div class="week-bar"><div class="week-date">Aug 14 -  18</div><div class="week-theme"><div class="theme-name">[ Electromagnetism ]</div><div class="theme-tag">Attracting al kinds of interesting things!</div></div></div><div class="week-stripe"></div></li>
    <li class="week"><div class="week-bar"><div class="week-date">Aug  21 - 25</div><div class="week-theme"><div class="theme-name">[ It's Hip to Be Healthy ]</div></div></div></li>
  </ol>

  <aside class="camp-panel">
    <div class="camp-intro">OUR PRE<br>SCHOOL'S</div>
    <div class="camp-season">summer</div>
    <div class="camp-word">CAMP</div>
    <div class="glassware" role="img" aria-label="Round flask, conical flask and measuring cylinder filled with light blue liquid"></div>
  </aside>

  <div class="footer-band"></div>
</main>
</body>
</html>
```